Need webpage for TUTORING COMPANY

Hello,
Our tutoring company Quillbrook Tutorials is launching a new program named 'Daylight Walk-Home Program'.
We would like a website created to showcase our new program.
Our current company page is: www.quillbrook.org
The new program webpage can have a link on the current company page that takes you to the new program webpage. We are open to ideas in regards to this. I would like the new program page to have the following:
-student online registration
-a way for parents to schedule their calendar days for the program
-a way for parents to pay (pricing is $45 a day or $745 per month)
The web content will be similar to this: http://pebblecoveclubhouse.com/
I personally did not like their website and I prefer a modern, sleek, structured, eye catchy design.
We need the website fairly quickly.
Thank you,
Varsha Menon
P.S: I am attaching the flyer & brochure for the new program.
School
After School Program by QuillBrook Tutoriails

```html
<!DOCTYPE html>
<html lang="en">
<head>
<meta charset="utf-8">
<title>Daylight Walk-Home Program</title>
<link href="https://fonts.googleapis.com/css2?family=Roboto:wght@400;500;700&display=swap" rel="stylesheet">
<style>
:root{
  --ink:#1c1c1c;
  --dark:#222222;
  --yellow:#f6c500;
  --white:#ffffff;
  --text:#555555;
  --muted:#8a8a8a;
  --field:#ffffff;
}
*{box-sizing:border-box;margin:0;padding:0}
html,body{width:811px;height:1200px;overflow:hidden}
body{font-family:'Roboto',Arial,sans-serif;background:var(--white);color:var(--text);position:relative}
.site-header{height:109px;background:var(--ink);position:relative;padding:14px 0 0 40px}
.program-title{color:var(--white);font-size:28px;font-weight:700;line-height:1.1}
.tagline{color:var(--yellow);font-size:11px;margin-top:3px}
.enrolling{color:#dddddd;font-size:10px;margin-top:2px}
.header-contact{position:absolute;right:40px;top:14px;text-align:right}
.phone{color:var(--white);font-size:11px}
.phone span{color:var(--yellow)}
.social{display:flex;gap:6px;justify-content:flex-end;margin-top:10px}
.social i{width:18px;height:18px;border-radius:50%;background:var(--white);display:block}
.main-nav{height:19px;background:var(--yellow);display:flex;padding-left:40px}
.main-nav a{font-size:9.5px;color:var(--ink);text-decoration:none;line-height:19px;padding:0 22px;border-right:1px solid rgba(0,0,0,.2)}
.main-nav a:first-child{padding-left:0}
.hero{position:relative;height:254px;background:linear-gradient(100deg,#e8c23a 0%,#c9a43a 35%,#7a8aa0 65%,#d8b63c 100%)}
.brand{position:absolute;left:12px;top:8px;display:flex;align-items:center;gap:6px;color:var(--white);font-weight:700;font-size:11px;letter-spacing:.5px}
.brand i{width:14px;height:14px;background:var(--white);display:block;border-radius:50%}
.hero-band{position:absolute;left:0;right:0;bottom:0;height:70px;background:rgba(0,0,0,.62);padding:10px 0 0 40px}
.hero-band h2{color:var(--white);font-size:19px;font-weight:500}
.hero-band p{color:#e0e0e0;font-size:9px;line-height:1.4;width:560px;margin-top:4px}
.pay-btn{position:absolute;right:40px;top:22px;background:var(--yellow);color:var(--ink);font-size:12px;font-weight:700;padding:7px 16px;border-radius:2px}
.services{position:absolute;left:74px;top:400px;display:flex;gap:17px}
.service{width:153px}
.service-tab{height:31px;background:var(--yellow);color:var(--ink);font-size:11px;font-weight:500;text-align:center;line-height:31px}
.service-card{margin-top:10px;background:var(--white);box-shadow:0 1px 5px rgba(0,0,0,.25);padding:14px 10px 14px;height:199px;text-align:center}
.service-photo{height:68px;background:linear-gradient(135deg,#c8dbe6,#e9d3b8)}
.service-card p{font-size:8.5px;line-height:1.45;margin-top:9px;color:var(--text)}
.read-more{display:inline-block;margin-top:8px;background:var(--ink);color:var(--white);font-size:8px;padding:4px 9px}
.about{position:absolute;top:672px;left:0;right:0;text-align:center}
.section-title{font-size:18px;font-weight:500;color:var(--ink)}
.rule{width:90px;height:2px;background:var(--yellow);margin:5px auto 0}
.body-copy{font-size:9px;line-height:1.9;width:700px;margin:16px auto 0;color:var(--text)}
.registration{position:absolute;top:805px;left:0;right:0;height:210px;background:var(--dark);text-align:center;padding-top:14px}
.registration .section-title{color:var(--yellow)}
.reg-form{display:grid;grid-template-columns:repeat(3,220px);gap:14px 35px;justify-content:center;margin-top:30px}
.field{height:22px;background:var(--field);font-size:9px;color:var(--muted);text-align:left;padding-left:8px;line-height:22px;position:relative}
.field.select::after{content:"";position:absolute;right:8px;top:9px;border:4px solid transparent;border-top-color:#444}
.send-btn{display:inline-block;margin-top:16px;background:var(--yellow);color:var(--ink);font-size:10px;font-weight:500;width:220px;height:22px;line-height:22px}
.schedule{position:absolute;top:1020px;left:0;right:0;text-align:center}
.schedule .body-copy{margin-top:14px}
.schedule-row{display:flex;justify-content:center;gap:12px;margin-top:16px}
.date-field{width:164px;height:24px;border:1px solid #cccccc;font-size:9px;color:var(--muted);text-align:left;padding-left:8px;line-height:22px}
.calendar-btn{width:96px;height:24px;background:var(--yellow);color:var(--ink);font-size:10px;font-weight:500;display:flex;align-items:center;justify-content:center;gap:5px}
.site-footer{position:absolute;bottom:0;left:0;right:0;height:27px;background:var(--ink);display:flex;align-items:center;justify-content:space-between;padding:0 30px}
.footer-nav a{color:var(--yellow);font-size:8.5px;text-decoration:none;margin-right:20px}
.copyright{color:#bbbbbb;font-size:8px}
</style>
</head>
<body>
<header class="site-header">
  <h1 class="program-title">Daylight Walk-Home Program</h1>
  <p class="tagline">Perfect Solution For Busy Parents</p>
  <p class="enrolling">Now Enrolling Grades K-8</p>
  <div class="header-contact">
    <p class="phone"><span>Phone:</span> (555)014-6211 | (555)014-7221</p>
    <div class="social"><i></i><i></i><i></i></div>
  </div>
</header>
<nav class="main-nav">
  <a href="#">Home</a><a href="#">About the Program</a><a href="#">Principle</a><a href="#">Calender</a><a href="#">Contact Us</a>
</nav>
<section class="hero" role="img" aria-label="Smiling schoolchildren boarding a yellow school bus">
  <div class="brand"><i></i>QUILLBROOK</div>
  <div class="hero-band">
    <h2>Pay For Your Kids</h2>
    <p>Lorem Ipsum is simply dummy text of the printing and typesetting industry. Lorem Ipsum has been the industry's standard dummy text ever since the 1500s, when an unknown printer took a galley of type and</p>
    <span class="pay-btn">PAY NOW!</span>
  </div>
</section>
<section class="services">
  <div class="service"><div class="service-tab">After School Pick Up</div><div class="service-card"><div class="service-photo" role="img" aria-label="Child with backpack at school"></div><p>There are many variations of passages of Lorem Ipsum available, but the majority have suffered alteration in some form.</p><span class="read-more">Read More</span></div></div>
  <div class="service"><div class="service-tab">Homework</div><div class="service-card"><div class="service-photo" role="img" aria-label="Student doing homework"></div><p>There are many variations of passages of Lorem Ipsum available, but the majority have suffered alteration in some form.</p><span class="read-more">Read More</span></div></div>
  <div class="service"><div class="service-tab">Enrichment Exercises</div><div class="service-card"><div class="service-photo" role="img" aria-label="Children in an enrichment activity"></div><p>There are many variations of passages of Lorem Ipsum available, but the majority have suffered alteration in some form.</p><span class="read-more">Read More</span></div></div>
  <div class="service"><div class="service-tab">Extra Curriculars</div><div class="service-card"><div class="service-photo" role="img" aria-label="Kids playing outdoor sports"></div><p>There are many variations of passages of Lorem Ipsum available, but the majority have suffered alteration in some form.</p><span class="read-more">Read More</span></div></div>
</section>
<section class="about">
  <h2 class="section-title">About Our Program</h2>
  <div class="rule"></div>
  <p class="body-copy">Lorem Ipsum is simply dummy text of the printing and typesetting industry. Lorem Ipsum has been the industry's standard dummy text ever since the 1500s, when an unknown printer took a galley of type and scrambled it to make a type specimen book. It has survived not only five centuries, but also the leap into electronic typesetting, remaining essentially unchanged.</p>
</section>
<section class="registration">
  <h2 class="section-title">Student Registration</h2>
  <div class="rule"></div>
  <div class="reg-form">
    <div class="field">Enter Student Name</div>
    <div class="field">Enter City</div>
    <div class="field select">Enter State</div>
    <div class="field">Enter Zip Code</div>
    <div class="field">Enter Phone No</div>
    <div class="field">Enter Grade Level</div>
  </div>
  <span class="send-btn">Send</span>
</section>
<section class="schedule">
  <h2 class="section-title">Schedule Your Calender</h2>
  <div class="rule"></div>
  <p class="body-copy">Lorem Ipsum is simply dummy text of the printing and typesetting industry. Lorem Ipsum has been the industry's standard dummy text ever since the 1500s, when an unknown printer took a galley of type and scrambled it to make a type specimen book. It has survived not only five centuries, but also the leap into electronic typesetting, remaining essentially unchanged.</p>
  <div class="schedule-row">
    <div class="date-field">Select Date</div>
    <div class="calendar-btn">
      <svg width="10" height="10" viewBox="0 0 10 10" aria-hidden="true"><rect x="0.5" y="1.5" width="9" height="8" fill="none" stroke="#1c1c1c"/><line x1="0.5" y1="4" x2="9.5" y2="4" stroke="#1c1c1c"/><line x1="3" y1="0" x2="3" y2="3" stroke="#1c1c1c"/><line x1="7" y1="0" x2="7" y2="3" stroke="#1c1c1c"/></svg>
      Calender
    </div>
  </div>
</section>
<footer class="site-footer">
  <nav class="footer-nav"><a href="#">Home</a><a href="#">About Our Program</a><a href="#">Principle</a><a href="#">Calender</a><a href="#">Contact Us</a></nav>
  <p class="copyright">&copy; Daylight Walk-Home Program All Rights Reserved</p>
</footer>
</body>
</html>
```